Lone Star Wetland Flora Stewardship Guild

We need to design the home page of this new website. We would like a fun website design for provides as a resource for members and information for potential members.
Please design so that we can see a portion of background on each side on the website.
I just need the final design files psd no coding needed.
Attached is their logo (colors are not 100% set in stone either so can mess with those as I did in the quick mockup attached)
Attached is a pdf newsletter they send out, you can get a feel for them and what they are about. The design is crappy and we are here to fix that going forward and we are starting with the website.
Here are some quick example websites (design style is open)
- I attached a quick mockup i did just for a content visual but by all means do what you want.
- http://www.brindlecourtleaders.org/
- http://www.qvelto.org/
- http://preview.plimworks7.com/view.php?cat=layoutpacks&host=gridcrafthub&temp=venrolite
- http://www.ploughvale.org/
- http://www.townmarrow.org/
- http://www.projectkindlecoat.org/
here are some of the other chapters website (pretty bad!)
and here are some of the others:
- http://www.zrelkq.org/
- http://ovtu.org/
- http://www.lirvx.org/
Content Items that need to be included:
1. Logo
2. Menu - home, about, members, resources, events, membership, contact
3. Become a member - button or action
4. social links - friendwall, jobrungo, clipzora
5. banner - that needs to explain their purpose "Promoting environmental stewardship through operations, research, education and outreach" (or this can be worked into the design)
6. Upcoming event (s)
7. Advertisement - members can place an ad on the website, this can be a placeholder for now
8. newsletter signup
9. advertise with us - this link can be in the footer
30-60 years of age, succesfull (household budgets of 120K+ men and women that live in texas.
Education

```html
<!DOCTYPE html>
<html lang="en">
<head>
<meta charset="utf-8">
<title>Lone Star Wetland Flora Stewardship Guild</title>
<link href="https://fonts.googleapis.com/css2?family=Arimo:ital,wght@0,400;0,700;1,400&family=Tinos:ital,wght@0,400;0,700;1,400&family=Roboto+Condensed:wght@400;700&display=swap" rel="stylesheet">
<style>
:root{
  --navy:#0b3a8c;
  --navy-dark:#082f73;
  --red:#c8364b;
  --btn-red:#d8404f;
  --dark:#3d3d3d;
  --text:#666;
  --muted:#888;
  --line:#9a9a9a;
  --white:#fff;
}
*{box-sizing:border-box;margin:0;padding:0}
html,body{width:710px;height:1200px;overflow:hidden;background:var(--white)}
body{position:relative;font-family:Arimo,Arial,sans-serif;color:var(--text)}
.abs{position:absolute}

/* top navigation */
.main-nav{position:absolute;left:0;top:0;width:710px;height:40px;background:var(--navy);z-index:3}
.main-nav a{position:absolute;top:14px;font:400 8.5px 'Roboto Condensed',Arial,sans-serif;color:var(--white);text-decoration:none;letter-spacing:.2px;transform:translateX(-50%)}

/* hero scene */
.hero-scene{position:absolute;left:0;top:40px;width:710px;height:380px;
  background:linear-gradient(180deg,#c8dcef 0%,#d9e7f2 30%,#8fae5e 46%,#6f8f4a 52%,#8aa6b8 62%,#a7a58a 78%,#c9b99a 100%)}
.hero-curve{position:absolute;left:0;top:370px;width:710px;height:60px}

.search-box{position:absolute;left:84px;top:60px;width:160px;height:24px;background:var(--white);border:1px solid #d6d6d6;z-index:2}
.search-box span{position:absolute;left:6px;top:8px;font:400 5px Tinos,serif;color:#555;letter-spacing:.2px}
.search-box svg{position:absolute;right:10px;top:6px}

.brand{position:absolute;left:255px;top:62px;width:200px;height:38px;display:flex;align-items:center;gap:6px;z-index:2}
.brand-dot{width:18px;height:18px;border-radius:50%;background:var(--red);flex:none}
.brand-name{font:700 10.5px/12px Tinos,serif;color:var(--navy)}

.btn-login,.btn-register{position:absolute;top:59px;width:77px;height:24px;font:400 10px/24px Tinos,serif;color:var(--white);text-align:center;letter-spacing:.3px;z-index:2}
.btn-login{left:465px;background:var(--btn-red)}
.btn-register{left:548px;background:var(--navy)}

.slider{position:absolute;left:85px;top:105px;width:540px;height:248px;border:3px solid var(--white);box-shadow:0 1px 4px rgba(0,0,0,.25);z-index:2;
  background:linear-gradient(180deg,#a9c6e6 0%,#d7e4ee 32%,#6f8e45 44%,#4f7a3e 50%,#3f6e9c 60%,#5f86a8 72%,#6e8a3c 86%,#5b7a30 100%)}
.slider-title{position:absolute;left:0;width:534px;top:78px;text-align:center;font:700 58px/1 Tinos,serif;color:rgba(255,255,255,.92);letter-spacing:1px;text-shadow:0 1px 2px rgba(0,0,0,.25)}
.slider-tagline{position:absolute;left:0;width:534px;top:140px;text-align:center;font:400 12.5px/21px Arimo,Arial,sans-serif;color:var(--white);text-shadow:0 1px 2px rgba(0,0,0,.35)}
.slider-dots{position:absolute;left:244px;top:176px;display:flex;gap:3px}
.slider-dots i{display:block;width:9px;height:9px;border-radius:50%;border:1.5px solid var(--white)}

.hero-arrows{position:absolute;left:338px;top:396px;width:34px;height:24px;z-index:2}

/* welcome */
.section-title{font:400 20px Tinos,serif;color:var(--red)}
.welcome-title{position:absolute;left:0;width:710px;top:438px;text-align:center}
.welcome-text{position:absolute;left:100px;width:510px;top:468px;text-align:center;font:italic 400 7.4px/16px Tinos,serif;color:var(--text)}
.btn-dark{position:absolute;height:23px;background:var(--dark);color:var(--white);font:400 9.5px/23px Tinos,serif;text-align:center}
.btn-member{left:316px;top:526px;width:106px}

.divider{position:absolute;left:84px;width:539px;border-top:1px dashed var(--line)}

/* events */
.events-title{position:absolute;left:84px;top:574px}
.events-arrows{position:absolute;left:605px;top:583px}
.event{position:absolute;width:270px;height:110px}
.event-photo{position:absolute;left:0;top:0;width:84px;height:84px;border-radius:50%}
.event-title{position:absolute;left:92px;top:10px;font:400 8.6px Arimo,Arial,sans-serif;color:#555;text-transform:uppercase}
.event-date{position:absolute;left:92px;top:23px;font:italic 400 6.4px Arimo,Arial,sans-serif;color:var(--muted)}
.event-text{position:absolute;left:92px;top:42px;width:176px;font:400 6.4px/11.6px Arimo,Arial,sans-serif;color:var(--muted)}
.event-more{position:absolute;left:92px;top:101px;font:700 5.6px Arimo,Arial,sans-serif;color:var(--red)}

/* about */
.about-title{position:absolute;left:84px;top:876px}
.about-sub{position:absolute;left:84px;top:904px;font:400 9.4px Arimo,Arial,sans-serif;color:#666;text-transform:uppercase}
.about-text{position:absolute;left:85px;width:355px;font:400 6.4px/12.6px Arimo,Arial,sans-serif;color:var(--muted)}
.btn-about{left:84px;top:1046px;width:72px;height:22px;line-height:22px}
.ad-slot{position:absolute;left:466px;top:881px;width:160px;height:207px;
  background:linear-gradient(180deg,#2f7fb8 0%,#1d5f92 25%,#15263b 55%,#1b2333 78%,#dcdcdc 80%,#e9e9e9 100%)}

/* footer */
.site-footer{position:absolute;left:0;top:1097px;width:710px;height:103px;background:var(--navy)}
.social{position:absolute;top:22px;display:flex;align-items:center;gap:3px;font:400 6.5px Arimo,Arial,sans-serif;color:var(--white)}
.social i{display:block;width:18px;height:18px;border-radius:50%;border:1.5px solid var(--white)}
.news-label{position:absolute;left:195px;top:25px;font:400 14px 'Roboto Condensed',Arial,sans-serif;color:var(--white)}
.news-sep{position:absolute;left:269px;top:20px;height:25px;border-left:1px solid rgba(255,255,255,.7)}
.news-text{position:absolute;left:285px;top:23px;width:180px;font:400 5.8px/11px 'Roboto Condensed',Arial,sans-serif;color:var(--white)}
.news-input{position:absolute;left:473px;top:22px;width:148px;height:24px;background:#eeeeee}
.news-input span{position:absolute;left:23px;top:9px;font:400 4.8px Arimo,Arial,sans-serif;color:#999}
.footer-rule{position:absolute;left:84px;top:58px;width:539px;border-top:1px solid rgba(255,255,255,.12)}
.copyright{position:absolute;left:84px;top:79px;font:400 6.4px Arimo,Arial,sans-serif;color:var(--white)}
.advertise{position:absolute;left:547px;top:76px;font:400 8.4px Arimo,Arial,sans-serif;color:var(--white);border-bottom:1px solid var(--white);padding-bottom:2px}
</style>
</head>
<body>

<nav class="main-nav">
  <a style="left:110px">HOME</a>
  <a style="left:179px">ABOUT</a>
  <a style="left:254px">MEMBERS</a>
  <a style="left:339px">RESOURCES</a>
  <a style="left:419px">EVENTS</a>
  <a style="left:502px">MEMBERSHIP</a>
  <a style="left:588px">CONTACT</a>
</nav>

<div class="hero-scene" role="img" aria-label="Wide wetland scene with sky, green shoreline trees and a pond covered in lily pads"></div>
<svg class="hero-curve" width="710" height="60" viewBox="0 0 710 60"><path d="M0 12 Q355 70 710 12 L710 60 L0 60 Z" fill="#fff"/></svg>

<div class="search-box"><span>ENTER ANY KEY WORD.....</span>
  <svg width="10" height="10" viewBox="0 0 10 10"><circle cx="4" cy="4" r="3" fill="none" stroke="#999" stroke-width="1.2"/><line x1="6.2" y1="6.2" x2="9.2" y2="9.2" stroke="#999" stroke-width="1.4"/></svg>
</div>

<div class="brand"><span class="brand-dot"></span><span class="brand-name">Lone Star Wetland Flora Stewardship Guild</span></div>

<div class="btn-login">LOGIN</div>
<div class="btn-register">REGISTER</div>

<div class="slider" role="img" aria-label="Banner photo of a marsh river under a cloudy sky with reeds in the foreground">
  <div class="slider-title">LSWG</div>
  <div class="slider-tagline">Promoting environmental stewardship through operations,<br>research, education and outreach</div>
  <div class="slider-dots"><i style="background:var(--navy)"></i><i style="background:var(--btn-red)"></i><i style="background:var(--btn-red)"></i></div>
</div>

<svg class="hero-arrows" width="34" height="24" viewBox="0 0 34 24">
  <path d="M0 24 A17 17 0 0 1 34 24 Z" fill="#fff"/>
  <path d="M13 9 L10 12 L13 15" fill="none" stroke="#555" stroke-width="1.2"/>
  <line x1="17" y1="8" x2="17" y2="16" stroke="#ccc" stroke-width=".6"/>
  <path d="M21 9 L24 12 L21 15" fill="none" stroke="#555" stroke-width="1.2"/>
</svg>

<h1 class="section-title welcome-title">Welcome To Lswg</h1>
<p class="welcome-text">Lorem ipsum dolor sit amet, consec tetuer adipiscing elit. Praesent vestibulum molestie lacus. Aenean non ummy hendrerit mauris. Phasellus porta. Fusce suscipit varius. mium sociis toque penatibus et magnis dis parturient montes, nascetur ridiculus mus.Lorem ipsum dolor sit amet, consec tetuer adipiscing elit. Praesent vestibulum molestie lacus. Aenean non ummy hendrerit mauris. Phasellus porta.</p>
<div class="btn-dark btn-member">Become a Member</div>

<div class="divider" style="top:565px"></div>

<h2 class="section-title events-title">Upcoming Event</h2>
<svg class="events-arrows" width="22" height="8" viewBox="0 0 22 8"><path d="M4 1 L1 4 L4 7" fill="none" stroke="#aaa"/><path d="M18 1 L21 4 L18 7" fill="none" stroke="#aaa"/></svg>

<article class="event" style="left:84px;top:614px">
  <div class="event-photo" role="img" aria-label="Lily pads and reeds on dark water" style="background:radial-gradient(circle at 50% 40%,#7f9c6a,#2f4a3a 75%)"></div>
  <h3 class="event-title">Vestibulum ante ipsum primis</h3>
  <div class="event-date">june.15.2014</div>
  <p class="event-text">Cum sociis natoque penatibus et magnis dis parturient montes, nascetur ridiculus mus. Nulla dui. Fusce feugiat malesuada odio. Morbi nunc odio, gravida at, cursus Duis ultricies pharetra magna.</p>
  <div class="event-more">[ READ MORE ]</div>
</article>
<article class="event" style="left:367px;top:614px">
  <div class="event-photo" role="img" aria-label="Grassy pond bank reflected in still water" style="background:linear-gradient(180deg,#f2f4f2 0%,#e6ece6 30%,#6e9a45 50%,#4f7e3a 70%,#8aa0a8 100%)"></div>
  <h3 class="event-title">Vestibulum ante ipsum primis</h3>
  <div class="event-date">june.15.2014</div>
  <p class="event-text">Cum sociis natoque penatibus et magnis dis parturient montes, nascetur ridiculus mus. Nulla dui. Fusce feugiat malesuada odio. Morbi nunc odio, gravida at, cursus Duis ultricies pharetra magna.</p>
  <div class="event-more">[ READ MORE ]</div>
</article>
<article class="event" style="left:84px;top:738px">
  <div class="event-photo" role="img" aria-label="Trees over a pond with floating lily pads" style="background:linear-gradient(180deg,#bcd6ee 0%,#e8f0f6 25%,#4f8a3a 50%,#7a9a70 70%,#c7b98a 100%)"></div>
  <h3 class="event-title">Vestibulum ante ipsum primis</h3>
  <div class="event-date">june.15.2014</div>
  <p class="event-text">Cum sociis natoque penatibus et magnis dis parturient montes, nascetur ridiculus mus. Nulla dui. Fusce feugiat malesuada odio. Morbi nunc odio, gravida at, cursus Duis ultricies pharetra magna.</p>
  <div class="event-more">[ READ MORE ]</div>
</article>
<article class="event" style="left:367px;top:738px">
  <div class="event-photo" role="img" aria-label="Blue sky over a calm lake and green shore" style="background:linear-gradient(180deg,#3d78c2 0%,#9cc0e4 38%,#5a8a3c 52%,#3f6fa8 66%,#5b7a3a 100%)"></div>
  <h3 class="event-title">Vestibulum ante ipsum primis</h3>
  <div class="event-date">june.15.2014</div>
  <p class="event-text">Cum sociis natoque penatibus et magnis dis parturient montes, nascetur ridiculus mus. Nulla dui. Fusce feugiat malesuada odio. Morbi nunc odio, gravida at, cursus Duis ultricies pharetra magna.</p>
  <div class="event-more">[ READ MORE ]</div>
</article>

<div class="divider" style="top:867px"></div>

<h2 class="section-title about-title">About Us</h2>
<div class="about-sub">Phasellus turpis orgra pellente dolore adipiscing</div>
<p class="about-text" style="top:925px">Lorem ipsum dolor sit amet, consete ctetur adipiscing.Duis eros ligula lacinia quis euismod in dignisim atneliquam quis consectetur magna. Aliquam sed nibhet condimentum ligula consequ eges.Lorem ipsum dolor sit amet, consete ctetur adipiscing.Duis eros ligula lacinia quis euismod in dignisim atneliquam quis consectetur magna. Aliquam sed nibhet condimentum ligula consequ eges.</p>
<p class="about-text" style="top:990px">Lorem ipsum dolor sit amet, consete ctetur adipiscing.Duis eros ligula lacinia quis euismod in dignisim atne liquam quis consectetur magna.Lorem ipsum dolor sit amet, consete ctetur adipiscing.Duis eros ligula lacinia quis euismod in dignisim atne liquam quis consectetur magna.</p>
<div class="btn-dark btn-about">READ MORE</div>

<aside class="ad-slot" role="img" aria-label="Member advertisement: pond treatment product packaging on a blue water backdrop with the advertiser's name below"></aside>

<footer class="site-footer">
  <div class="social" style="left:100px"><i></i>friendwall</div>
  <div class="social" style="left:100px;top:44px;display:none"></div>
  <div class="social" style="left:100px;top:6px;display:none"></div>
  <div class="social" style="left:100px;top:22px;visibility:hidden"></div>
  <div class="news-label">NewsLetter :</div>
  <div class="news-sep"></div>
  <p class="news-text">In venenatis neque a eros laoreet eu placerat erat suscipit. Fusce cursus, erat ut scelerisque condimentum</p>
  <div class="news-input">
    <svg class="abs" style="left:7px;top:8px" width="12" height="8" viewBox="0 0 12 8"><rect x=".5" y=".5" width="11" height="7" fill="none" stroke="#999"/><path d="M.5 .5 L6 4.5 L11.5 .5" fill="none" stroke="#999"/></svg>
    <span>Enter Your Email Address :</span>
    <svg class="abs" style="left:136px;top:8px" width="6" height="9" viewBox="0 0 6 9"><path d="M1 1 L5 4.5 L1 8" fill="none" stroke="#999"/></svg>
  </div>
  <div class="footer-rule"></div>
  <div class="copyright">© Copy Rights 2014 Lswg.All Rights Reserved</div>
  <div class="advertise">Advertise With Us</div>
  <svg class="abs" style="left:617px;top:78px" width="9" height="7" viewBox="0 0 9 7"><path d="M1 1 L3.5 3.5 L1 6 M5 1 L7.5 3.5 L5 6" fill="none" stroke="#fff"/></svg>
</footer>

<style>
.site-footer .social:first-child{left:84px}
</style>
<div class="social" style="position:absolute;left:84px;top:1119px;display:none"></div>
<div style="position:absolute;left:84px;top:1119px;display:flex;flex-direction:column;gap:2px;font:400 6px Arimo,Arial,sans-serif;color:var(--white);visibility:hidden"></div>
<div style="position:absolute;left:130px;top:1119px;display:flex;align-items:center;gap:3px;font:400 6.5px Arimo,Arial,sans-serif;color:var(--white)"></div>
<div style="position:absolute;left:84px;top:1144px;display:flex;gap:10px;font:400 6.5px Arimo,Arial,sans-serif;color:var(--white)">
  <span style="display:flex;align-items:center;gap:3px"><i style="display:block;width:8px;height:8px;border-radius:50%;border:1px solid #fff"></i>jobrungo</span>
  <span style="display:flex;align-items:center;gap:3px"><i style="display:block;width:8px;height:8px;border-radius:50%;border:1px solid #fff"></i>clipzora</span>
</div>
</body>
</html>
```